Tidal Sparks - Main Menu - Re-Design

I want to have a refresh for this app's main menu. There are some different items on the menu depending on the language (English vs. Non-English) and version (Pro vs. Free). I have attached screenshots of the different conditions. This app is a collection of brain training games.

Need designs for light and dark mode. Need designs for both portrait and landscape mode.

Here is a link to the app in Brisk Market.
https://apps.briskmarket.example/store/apps/details?id=tidalworks.tidalsparks

Here is a link to the app in the Orvel App Store.
https://depot.orvel.example/us/app/tidal-sparks-focus-drills/id519274063?ls=1&mt=8

```html
<!DOCTYPE html>
<html lang="en">
<head>
<meta charset="utf-8">
<title>Tidal Sparks App (Free) – Redesign</title>
<link rel="stylesheet" href="https://fonts.googleapis.com/css2?family=Poppins:wght@300;400;500;600&display=swap">
<style>
:root{
  --stage:#cfd0e8;
  --ink-light:#2a2a2e;
  --muted:#8a8a92;
  --screen-light:#f5f4f8;
  --screen-dark:#1b1b1d;
  --adbar:#f8f8fa;
  --blue:#7ca6d0;
  --purple:#b49ad9;
  --periwinkle:#98a2e0;
  --gray:#9d9d9f;
  --pink:#e98e97;
  --sand:#ead196;
  --green:#6fae74;
  --white:#ffffff;
}
*{box-sizing:border-box;margin:0;padding:0}
html,body{width:1200px;height:840px;overflow:hidden}
body{background:var(--stage);font-family:"Poppins",sans-serif;position:relative}
.board-title{position:absolute;top:50px;left:0;width:1200px;text-align:center;color:var(--white);font-weight:600;font-size:36px;letter-spacing:.08em}
.mode-label{position:absolute;top:752px;width:300px;text-align:center;color:var(--white);font-weight:300;font-size:25px;letter-spacing:.16em}
.mode-label.light{left:179px}
.mode-label.dark{left:738px}

.screen{position:absolute;overflow:hidden;border-radius:18px;background:var(--screen-light);color:var(--ink-light)}
.screen.dark{background:var(--screen-dark);color:var(--white)}
.screen.portrait{width:139px;height:304px;top:185px}
.screen.landscape{width:301px;height:140px;top:565px;border-radius:16px}

.status{position:absolute;top:5px;left:0;right:0;height:6px;font-size:3.6px;font-weight:500}
.status .clock{position:absolute;left:19px}
.status .signal{position:absolute;right:14px;top:1px;width:14px;height:3px;background:linear-gradient(90deg,currentColor 0 40%,transparent 40% 55%,currentColor 55% 100%);border-radius:1px}

.greeting{position:absolute;top:21px;left:8px;font-size:4.4px;color:var(--muted)}
.dark .greeting{color:#d9d9de}
.user-name{position:absolute;top:28px;left:8px;font-size:7.4px;font-weight:600}
.toggle{position:absolute;top:42px;left:8px;width:15px;height:7px;border-radius:4px;background:#e4e3ea}
.toggle::after{content:"";position:absolute;top:1px;left:1px;width:5px;height:5px;border-radius:50%;background:var(--white);box-shadow:0 0 1px rgba(0,0,0,.3)}
.dark .toggle{background:transparent;border:1px solid var(--white)}
.dark .toggle::after{left:auto;right:1px;top:.5px;width:4.5px;height:4.5px}
.avatar{position:absolute;top:22px;right:8px;width:22px;height:22px;border-radius:50%;background:radial-gradient(circle at 50% 40%,#5a4a3e 0 35%,#78a7d6 36%)}
.avatar-badge{position:absolute;top:39px;right:26px;width:6px;height:6px;border-radius:50%;background:#1f5f9c;border:1px solid var(--white)}
.divider{position:absolute;top:51px;left:8px;right:8px;height:1px;background:#dedde5}
.dark .divider{background:#e8e8ec}

.menu{position:absolute;top:59px;left:8px;right:8px;display:flex;flex-direction:column;gap:12px}
.menu-card{position:relative;height:44px;border-radius:4px;color:var(--white);padding:0 7px;display:flex;flex-direction:column;justify-content:center;box-shadow:0 3px 6px rgba(60,60,110,.18);flex:none}
.menu-card.peek{height:20px}
.card-title{font-size:7px;font-weight:600;letter-spacing:.07em;text-transform:uppercase;line-height:1.05}
.card-sub{font-size:3.8px;margin-top:2px;opacity:.9}
.card-art{position:absolute;right:7px;top:7px;width:32px;height:30px;border-radius:8px}
.card-games{background:var(--blue)}
.card-training{background:var(--purple)}
.card-schedule{background:var(--periwinkle)}
.card-settings{background:var(--gray)}
.card-learning{background:var(--pink)}
.card-scores{background:var(--sand)}
.card-extra{background:var(--green)}
.art-games{background:radial-gradient(ellipse at 50% 55%,#2b3450 0 40%,#5b7fd6 60%,transparent 72%)}
.art-training{background:radial-gradient(ellipse at 55% 50%,#f4e9f0 0 35%,#9a6fd0 55%,transparent 72%)}
.art-schedule{background:radial-gradient(ellipse at 55% 55%,#fbf3ec 0 35%,#e25b6a 55%,transparent 72%)}
.art-settings{background:radial-gradient(ellipse at 35% 50%,#f2b733 0 30%,transparent 45%),radial-gradient(ellipse at 72% 55%,#4d7ee0 0 25%,transparent 40%)}
.art-learning{background:radial-gradient(ellipse at 65% 35%,#fde9ee 0 25%,transparent 40%),radial-gradient(ellipse at 40% 75%,#f3a3b4 0 20%,transparent 40%)}
.art-scores{background:radial-gradient(ellipse at 50% 60%,#f4f0e6 0 30%,#c99a35 50%,transparent 70%)}

.adbar{position:absolute;left:0;right:0;bottom:0;height:19px;background:var(--adbar);color:#2a2a2e;font-size:6px;font-weight:500;display:flex;align-items:center;justify-content:center}
.adbar .close{position:absolute;left:10px;top:6px;width:7px;height:7px}

.landscape .greeting{left:0;right:0;top:12px;text-align:center}
.landscape .user-name{left:0;right:0;top:18px;text-align:center}
.landscape .toggle{top:14px;left:13px}
.landscape .avatar{top:7px;right:14px}
.landscape .avatar-badge{top:23px;right:32px}
.landscape .divider{top:33px;left:14px;right:14px}
.landscape .menu{top:46px;left:14px;right:14px;gap:13px}
.landscape .menu-card{height:46px;padding:0 18px}
.landscape .menu-card.peek{height:20px;justify-content:flex-start;padding-top:9px}
.landscape .card-title{font-size:9px}
.landscape .card-sub{font-size:4.6px}
.landscape .card-art{right:18px;top:4px;width:58px;height:38px}
.landscape .peek .card-art{top:4px;width:22px;height:14px;right:24px}
.landscape .adbar{height:20px}
.landscape .adbar .close{left:14px;top:6.5px}
</style>
</head>
<body>
<h1 class="board-title">TIDAL SPARKS APP (FREE) - REDESIGN</h1>

<svg width="0" height="0" style="position:absolute" aria-hidden="true">
  <symbol id="icon-close" viewBox="0 0 10 10"><circle cx="5" cy="5" r="5" fill="#8a8a92"/><path d="M3.3 3.3l3.4 3.4M6.7 3.3L3.3 6.7" stroke="#fff" stroke-width="1.2" stroke-linecap="round"/></symbol>
</svg>

<!-- Light · Spanish -->
<section class="screen portrait" style="left:147px">
  <div class="status"><span class="clock">9:41</span><span class="signal"></span></div>
  <p class="greeting">Bienvenido de nuevo,</p>
  <p class="user-name">Invitado</p>
  <span class="toggle"></span>
  <div class="avatar" role="img" aria-label="Illustrated user avatar"></div><span class="avatar-badge"></span>
  <div class="divider"></div>
  <div class="menu">
    <div class="menu-card card-games"><p class="card-title">Lista de juegos</p><p class="card-sub">Ejercita tu memoria cerebral</p><div class="card-art art-games" role="img" aria-label="3D game controller illustration"></div></div>
    <div class="menu-card card-training"><p class="card-title">Centro de<br>entrenamiento</p><p class="card-sub">Hacer ejercicio regularmente</p><div class="card-art art-training" role="img" aria-label="3D clipboard with tick illustration"></div></div>
    <div class="menu-card card-schedule"><p class="card-title">Programa</p><p class="card-sub">Establece tu horario</p><div class="card-art art-schedule" role="img" aria-label="3D calendar illustration"></div></div>
    <div class="menu-card card-settings"><p class="card-title">Settings</p><p class="card-sub">Haz tu propio ajuste</p><div class="card-art art-settings" role="img" aria-label="3D gears illustration"></div></div>
    <div class="menu-card card-extra peek"></div>
  </div>
  <div class="adbar"><svg class="close"><use href="#icon-close"/></svg>Space for Ads</div>
</section>

<!-- Light · English -->
<section class="screen portrait" style="left:376px">
  <div class="status"><span class="clock"></span><span class="signal" style="opacity:0"></span></div>
  <p class="greeting">Welcome back,</p>
  <p class="user-name">Guest</p>
  <span class="toggle"></span>
  <div class="avatar" role="img" aria-label="Illustrated user avatar"></div><span class="avatar-badge"></span>
  <div class="divider"></div>
  <div class="menu">
    <div class="menu-card card-games"><p class="card-title">Game list</p><p class="card-sub">Exercise your brain memory</p><div class="card-art art-games" role="img" aria-label="3D game controller illustration"></div></div>
    <div class="menu-card card-training"><p class="card-title">Training centre</p><p class="card-sub">Exercise regularly</p><div class="card-art art-training" role="img" aria-label="3D clipboard with tick illustration"></div></div>
    <div class="menu-card card-learning"><p class="card-title">Learning</p><p class="card-sub">Find lots of learning</p><div class="card-art art-learning" role="img" aria-label="3D cloud and hearts illustration"></div></div>
    <div class="menu-card card-scores"><p class="card-title">Scores</p><p class="card-sub">Find the top score here</p><div class="card-art art-scores" role="img" aria-label="3D trophies on podium illustration"></div></div>
    <div class="menu-card card-schedule peek"></div>
  </div>
  <div class="adbar"><svg class="close"><use href="#icon-close"/></svg>Space for Ads</div>
</section>

<!-- Dark · English -->
<section class="screen portrait dark" style="left:722px">
  <div class="status"><span class="clock">9:41</span><span class="signal"></span></div>
  <p class="greeting">Welcome back,</p>
  <p class="user-name">Guest</p>
  <span class="toggle"></span>
  <div class="avatar" role="img" aria-label="Illustrated user avatar"></div><span class="avatar-badge"></span>
  <div class="divider"></div>
  <div class="menu">
    <div class="menu-card card-games"><p class="card-title">Game list</p><p class="card-sub">Exercise your brain memory</p><div class="card-art art-games" role="img" aria-label="3D game controller illustration"></div></div>
    <div class="menu-card card-training"><p class="card-title">Training centre</p><p class="card-sub">Exercise regularly</p><div class="card-art art-training" role="img" aria-label="3D clipboard with tick illustration"></div></div>
    <div class="menu-card card-learning"><p class="card-title">Learning</p><p class="card-sub">Find lots of learning</p><div class="card-art art-learning" role="img" aria-label="3D cloud and hearts illustration"></div></div>
    <div class="menu-card card-scores"><p class="card-title">Scores</p><p class="card-sub">Find the top score here</p><div class="card-art art-scores" role="img" aria-label="3D trophies on podium illustration"></div></div>
    <div class="menu-card card-schedule peek"></div>
  </div>
  <div class="adbar"><svg class="close"><use href="#icon-close"/></svg>Space for Ads</div>
</section>

<!-- Dark · Spanish -->
<section class="screen portrait dark" style="left:914px">
  <div class="status"><span class="clock">9:41</span><span class="signal"></span></div>
  <p class="greeting">Bienvenido de nuevo,</p>
  <p class="user-name">Invitado</p>
  <span class="toggle"></span>
  <div class="avatar" role="img" aria-label="Illustrated user avatar"></div><span class="avatar-badge"></span>
  <div class="divider"></div>
  <div class="menu">
    <div class="menu-card card-games"><p class="card-title">Lista de juegos</p><p class="card-sub">Ejercita tu memoria cerebral</p><div class="card-art art-games" role="img" aria-label="3D game controller illustration"></div></div>
    <div class="menu-card card-training"><p class="card-title">Centro de<br>entrenamiento</p><p class="card-sub">Hacer ejercicio regularmente</p><div class="card-art art-training" role="img" aria-label="3D clipboard with tick illustration"></div></div>
    <div class="menu-card card-schedule"><p class="card-title">Programa</p><p class="card-sub">Establece tu horario</p><div class="card-art art-schedule" role="img" aria-label="3D calendar illustration"></div></div>
    <div class="menu-card card-settings"><p class="card-title">Settings</p><p class="card-sub">Haz tu propio ajuste</p><div class="card-art art-settings" role="img" aria-label="3D gears illustration"></div></div>
    <div class="menu-card card-extra peek"></div>
  </div>
  <div class="adbar"><svg class="close"><use href="#icon-close"/></svg>Space for Ads</div>
</section>

<!-- Light · Landscape -->
<section class="screen landscape" style="left:183px">
  <span class="toggle"></span>
  <p class="greeting">Bienvenido de nuevo,</p>
  <p class="user-name">Invitado</p>
  <div class="avatar" role="img" aria-label="Illustrated user avatar"></div><span class="avatar-badge"></span>
  <div class="divider"></div>
  <div class="menu">
    <div class="menu-card card-games"><p class="card-title">Lista de juegos</p><p class="card-sub">Exercise your brain memory</p><div class="card-art art-games" role="img" aria-label="3D game controller illustration"></div></div>
    <div class="menu-card card-training peek"><p class="card-title">Centro de entrenamiento</p><div class="card-art art-training" role="img" aria-label="3D clipboard with tick illustration"></div></div>
  </div>
  <div class="adbar"><svg class="close"><use href="#icon-close"/></svg>Space for Ads</div>
</section>

<!-- Dark · Landscape -->
<section class="screen landscape dark" style="left:741px">
  <span class="toggle"></span>
  <p class="greeting">Bienvenido de nuevo,</p>
  <p class="user-name">Invitado</p>
  <div class="avatar" role="img" aria-label="Illustrated user avatar"></div><span class="avatar-badge"></span>
  <div class="divider"></div>
  <div class="menu">
    <div class="menu-card card-games"><p class="card-title">Lista de juegos</p><p class="card-sub">Exercise your brain memory</p><div class="card-art art-games" role="img" aria-label="3D game controller illustration"></div></div>
    <div class="menu-card card-training peek"><p class="card-title">Centro de entrenamiento</p><div class="card-art art-training" role="img" aria-label="3D clipboard with tick illustration"></div></div>
  </div>
  <div class="adbar"><svg class="close"><use href="#icon-close"/></svg>Space for Ads</div>
</section>

<p class="mode-label light">LIGHT MODE</p>
<p class="mode-label dark">DARK MODE</p>
</body>
</html>
```